Velmorytrips.com web design project + logo design

Hi,

We are a Russian online tour operator - roamquiltex.com

We are looking to tranmsfer our domain to velmorytrips.com. The website and logo need to be velmoryesque - we are not looking to change our functionality, but we need to make the website much more attracitve to clients, much more wild looking but at the same time remaining a professional travel company.

The main concept of the website should be innovative travel (as velmory was an innovator). Alternatively, you could go down the artist route and go down the draw / design your own tour road.

On our website the customer is able to combine travel services (hotels, flights, Visa services, and soon chauffeur, car rental etc...) put it into their basket (the basket definitely has to look better than it is at the moment) and pay for it in one go by card.

We are also stressin our customer support with web chat, call centre etc... (call centre number at the top of the page)

We aim to provide an easy user experience, but we need to make it have some more style, so I will be waiting for what you guys can come up with.
Let me know if you have any questions - skype is: mrkostelin

Industry/Entity Type

It Company

Logo Text

Requirements
Must have
• It is quite a simple task - to take the existing website roamquiltex.com and velmorysize it to create velmorytrips.com, the functionality of the website will remain the same and there are not many pages in the website. Homepage, Checkout step1, Checkout step 2 (you can view both of these if you select a service) and the generic pages for T&C''s, Privacy policy etc...

IMPORTANT UPDATE

We are also looking at how the search results will look in the designs, (please do a search on our website for hotel / flight)

```html
<!DOCTYPE html>
<html lang="en">
<head>
<meta charset="utf-8">
<title>Velmorytrips.com — Home</title>
<link href="https://fonts.googleapis.com/css2?family=Ubuntu:wght@400;500&family=Roboto:wght@300;400&family=PT+Serif:ital@0;1&display=swap" rel="stylesheet">
<style>
:root{
  --brand-blue:#0f7cc9;
  --brand-blue-dark:#0a5fa3;
  --nav-blue:#1384d3;
  --ink:#3a3a3a;
  --muted:#8a9299;
  --page:#edf1f3;
  --panel:#dde3e7;
  --green:#5dbb2c;
  --green-dark:#3f9d15;
  --footer:#1e1e1e;
  --white:#ffffff;
}
*{box-sizing:border-box;margin:0;padding:0}
html,body{width:1107px;height:1200px;overflow:hidden}
body{position:relative;background:var(--page);font-family:"Roboto",sans-serif;color:var(--ink)}
.abs{position:absolute}

.top-rule{left:0;top:0;width:1107px;height:5px;background:var(--brand-blue)}
.header{left:0;top:5px;width:1107px;height:121px;background:linear-gradient(#ffffff,#f1f3f4)}
.brand{left:101px;top:72px;display:flex;align-items:center;gap:8px}
.brand-dot{width:22px;height:22px;border-radius:50%;background:var(--brand-blue)}
.brand-name{font-family:"Ubuntu",sans-serif;font-weight:500;font-size:22px;color:var(--brand-blue-dark)}
.contact{right:104px;top:24px;text-align:right;font-family:"Ubuntu",sans-serif}
.contact-note{font-size:14px;color:#2c3e50;display:flex;align-items:center;gap:6px;justify-content:flex-end}
.contact-phone{font-size:15.5px;color:var(--brand-blue);margin-top:3px}
.search{left:810px;top:87px;width:193px;height:26px;background:#fff;border:1px solid #e0e4e6;border-radius:3px;font-family:"Ubuntu",sans-serif;font-size:11px;color:#c3c7ca;padding:7px 8px}
.search svg{position:absolute;right:6px;top:4px}

.hero{left:0;top:126px;width:1107px;height:384px}
.nav{left:101px;top:126px;width:904px;height:38px;background:linear-gradient(var(--nav-blue),#0c6fb8);font-family:"Ubuntu",sans-serif;font-size:13px;color:#fff}
.nav-item{position:absolute;top:12px;transform:translateX(-50%);white-space:nowrap}
.nav-item.current{font-weight:500}
.nav-sep{position:absolute;top:8px;width:1px;height:22px;background:rgba(255,255,255,.25)}

.booking{left:761px;top:201px;width:227px;height:297px;background:rgba(20,20,20,.82);font-family:"Ubuntu",sans-serif;color:#fff}
.booking-title{position:absolute;left:12px;top:20px;font-size:14.5px;display:flex;align-items:center;gap:8px}
.field{position:absolute;left:11px;width:209px;height:20px;background:linear-gradient(#fff,#e9ecee);border-radius:2px;font-size:11px;color:var(--brand-blue);padding:4px 8px}
.field::after,.mini-select::after{content:"";position:absolute;right:8px;top:8px;border:4px solid transparent;border-top-color:#9aa3a9}
.row-label{position:absolute;left:14px;font-size:11.5px}
.mini-select{position:absolute;top:172px;width:70px;height:19px;background:linear-gradient(#fff,#e9ecee);border-radius:2px;font-size:10px;color:var(--brand-blue);padding:4px 5px}
.check{position:absolute;left:58px;font-size:11px;display:flex;align-items:center;gap:8px}
.box{width:9px;height:9px;background:#fff;border-radius:1px;position:relative}
.btn-avail{position:absolute;left:21px;top:243px;width:187px;height:29px;border-radius:3px;background:linear-gradient(#8ddc4f,var(--green-dark));font-size:16px;text-align:center;line-height:29px;color:#fff}

.section-title{left:101px;top:524px;font-family:"Ubuntu",sans-serif;font-size:18.5px;color:var(--brand-blue)}
.hatch{left:216px;top:530px;width:447px;height:10px;background:repeating-linear-gradient(135deg,#d3d9dd 0 2px,transparent 2px 4px)}
.pager{left:676px;top:530px;display:flex;gap:5px}
.service-name{left:101px;top:559px;font-family:"Ubuntu",sans-serif;font-size:14px;color:#444}
.service-sub{left:101px;top:580px;font-size:11px;color:var(--muted);font-weight:300}
.btn-gallery{left:101px;top:607px;width:189px;height:27px;background:var(--green);color:#fff;font-size:11.5px;font-weight:300;line-height:27px;padding-left:12px}
.amenity{width:52px;text-align:center;top:651px}
.amenity-icon{width:50px;height:50px;border-radius:50%;background:#d9dfe3;border:2px solid #eef1f3;display:flex;align-items:center;justify-content:center;margin:0 auto}
.amenity-label{font-family:"PT Serif",serif;font-size:11.5px;color:#3c6a8f;margin-top:13px;line-height:22px}
.room-frame{left:323px;top:558px;width:378px;height:194px;background:#fff;padding:4px;box-shadow:0 0 0 1px #d7dde1}
.room-photo{width:100%;height:100%;background:linear-gradient(135deg,#c9a06e 0%,#8a5a3a 40%,#3f5e7a 70%,#d8c6a4 100%)}
.price-tag{left:583px;top:573px;width:125px;height:27px;background:var(--brand-blue);color:#fff;font-family:"Ubuntu",sans-serif;font-style:italic;font-size:15px;line-height:27px;padding-left:12px}
.price-tag::after{content:"";position:absolute;right:0;bottom:-6px;border-left:6px solid #0a4f86;border-bottom:6px solid transparent}
.intro{left:107px;top:772px;width:590px;font-size:11.5px;font-weight:300;line-height:17.5px;color:#7d868d}
.divider{left:107px;top:853px;width:590px;height:1px;background:#dfe4e7}

.aside{left:726px;top:519px;width:277px;height:259px;background:var(--panel)}
.aside-card{position:absolute;left:17px;top:17px;width:243px;height:65px;background:#fff}
.aside-mark{position:absolute;left:3px;top:3px;width:78px;height:59px;background:#eef2f4;display:flex;align-items:center;justify-content:center}
.aside-mark span{width:26px;height:26px;border-radius:50%;background:var(--brand-blue)}
.aside-title{position:absolute;left:86px;top:6px;font-family:"Ubuntu",sans-serif;font-size:15.5px;color:var(--brand-blue)}
.aside-text{position:absolute;left:17px;top:101px;width:245px;font-size:11px;font-weight:300;line-height:17px;color:#7f888f}
.aside-more{position:absolute;left:18px;top:216px;font-family:"PT Serif",serif;font-style:italic;font-size:11.5px;color:#333}

.gallery{left:99px;top:877px;width:904px;height:248px;background:var(--panel)}
.card{position:absolute;top:27px;width:195px}
.card-photo{height:117px;border:4px solid #fff;box-shadow:0 0 0 1px #cfd6da}
.card-title{font-family:"Ubuntu",sans-serif;font-size:12.5px;color:var(--brand-blue);margin-top:11px;padding-left:2px}
.card-text{font-size:11.5px;line-height:14.5px;color:#333;margin-top:7px;padding-left:2px;font-weight:300}
.arrow{width:26px;height:26px;background:var(--brand-blue);display:flex;align-items:center;justify-content:center}

.footer{left:0;top:1155px;width:1107px;height:45px;background:var(--footer);color:#cfcfcf;font-family:"Ubuntu",sans-serif;font-size:12.5px;text-align:center;line-height:45px}
</style>
</head>
<body>
<div class="abs top-rule"></div>
<header class="abs header"></header>
<div class="abs brand"><span class="brand-dot"></span><span class="brand-name">velmorytrips.com</span></div>
<div class="abs contact">
  <div class="contact-note"><svg width="13" height="13" viewBox="0 0 24 24"><path fill="#2c4a6b" d="M6.6 10.8a15 15 0 0 0 6.6 6.6l2.2-2.2c.3-.3.7-.4 1-.2 1.1.4 2.3.6 3.6.6.6 0 1 .4 1 1V20c0 .6-.4 1-1 1A17 17 0 0 1 3 4c0-.6.4-1 1-1h3.5c.6 0 1 .4 1 1 0 1.2.2 2.4.6 3.6.1.3 0 .7-.2 1z"/></svg>You call, we're there</div>
  <div class="contact-phone">+7 (495) 000-41-26</div>
</div>
<div class="abs search">Search<svg width="18" height="18" viewBox="0 0 20 20"><circle cx="8" cy="8" r="6" fill="none" stroke="#2aa0e6" stroke-width="2.4"/><path d="M12.5 12.5 18 18" stroke="#2aa0e6" stroke-width="2.6" stroke-linecap="round"/></svg></div>

<svg class="abs hero" viewBox="0 0 1107 384" role="img" aria-label="Photo of a Greek island harbour town with colourful houses, blue sky and sea">
  <defs>
    <linearGradient id="sky" x1="0" y1="0" x2="0" y2="1">
      <stop offset="0" stop-color="#2f72c4"/><stop offset=".35" stop-color="#a9c7e6"/>
      <stop offset=".55" stop-color="#cdbf9e"/><stop offset=".66" stop-color="#3e78b8"/>
      <stop offset="1" stop-color="#123e7a"/>
    </linearGradient>
  </defs>
  <path d="M0 0H1107V384Q900 350 760 352Q560 340 380 352Q150 360 0 384Z" fill="url(#sky)"/>
</svg>

<nav class="abs nav">
  <span class="nav-item current" style="left:41px">HOME</span>
  <span class="nav-sep" style="left:111px"></span>
  <span class="nav-item" style="left:197px">Destinations</span>
  <span class="nav-sep" style="left:282px"></span>
  <span class="nav-item" style="left:359px">Activities</span>
  <span class="nav-sep" style="left:436px"></span>
  <span class="nav-item" style="left:515px">Trip Styles</span>
  <span class="nav-sep" style="left:593px"></span>
  <span class="nav-item" style="left:679px">Responsible</span>
  <span class="nav-sep" style="left:766px"></span>
  <span class="nav-item" style="left:833px">Travel</span>
</nav>

<form class="abs booking">
  <div class="booking-title"><svg width="18" height="16" viewBox="0 0 18 16"><circle cx="6" cy="5" r="3.5" fill="none" stroke="#fff" stroke-width="1.5"/><path d="M1 15c0-3 2.3-5 5-5s5 2 5 5" fill="none" stroke="#fff" stroke-width="1.5"/><circle cx="13" cy="6" r="2.5" fill="#fff"/></svg>Check Availablity</div>
  <div class="field" style="top:54px">Откуда</div>
  <div class="field" style="top:81px">Куда</div>
  <div class="field" style="top:110px">Туда</div>
  <div class="field" style="top:138px">Обратно</div>
  <span class="row-label" style="top:175px">Пассажиры</span>
  <div class="mini-select" style="left:78px">select</div>
  <div class="mini-select" style="left:150px">select</div>
  <span class="row-label" style="top:209px">Класс</span>
  <span class="check" style="top:208px"><span class="box"></span>Обратно</span>
  <span class="check" style="top:225px"><span class="box"><svg width="9" height="9" viewBox="0 0 9 9" style="position:absolute;left:0;top:0"><path d="M1.5 4.5 3.5 6.5 7.5 2" fill="none" stroke="#222" stroke-width="1.6"/></svg></span>В одну сторону</span>
  <div class="btn-avail">View Availablity</div>
</form>

<h2 class="abs section-title">Our Services</h2>
<div class="abs hatch"></div>
<div class="abs pager"><svg width="8" height="9"><path d="M7 0 0 4.5 7 9Z" fill="#9aa3a9"/></svg><svg width="8" height="9"><path d="M1 0 8 4.5 1 9Z" fill="#9aa3a9"/></svg></div>
<h3 class="abs service-name">Hoteling Services</h3>
<p class="abs service-sub">Lorem Ipsum is simply dummy text</p>
<div class="abs btn-gallery">The bed Rooms show on Gallery</div>

<div class="abs amenity" style="left:106px">
  <div class="amenity-icon"><svg width="28" height="26" viewBox="0 0 28 26"><path d="M14 1 1 13h4v12h7v-8h4v8h7V13h4z" fill="#2b2b2b"/></svg></div>
  <div class="amenity-label">4500 sq<br>ft</div>
</div>
<div class="abs amenity" style="left:169px">
  <div class="amenity-icon"><svg width="32" height="20" viewBox="0 0 32 20"><path d="M2 3v15M30 9v9M2 13h28" stroke="#2b2b2b" stroke-width="2.5" fill="none"/><rect x="4" y="6" width="8" height="5" rx="2" fill="#2b2b2b"/><path d="M13 11V8h15l2 3z" fill="#2b2b2b"/></svg></div>
  <div class="amenity-label">5 Beds</div>
</div>
<div class="abs amenity" style="left:231px">
  <div class="amenity-icon"><svg width="28" height="28" viewBox="0 0 28 28"><path d="M6 26V10a7 7 0 0 1 14 0" fill="none" stroke="#2b2b2b" stroke-width="2.6"/><path d="M15 12h10l-5-5z" fill="#2b2b2b"/><g fill="#2b2b2b"><circle cx="17" cy="17" r="1.2"/><circle cx="21" cy="16" r="1.2"/><circle cx="24" cy="19" r="1.2"/><circle cx="19" cy="21" r="1.2"/><circle cx="23" cy="23" r="1.2"/></g></svg></div>
  <div class="amenity-label">2 Baths</div>
</div>

<div class="abs room-frame"><div class="room-photo" role="img" aria-label="Photo of a hotel bedroom with a striped bed, lamps and a desk"></div></div>
<div class="abs price-tag">$ 325.500</div>
<p class="abs intro">Aliquam erat volutpat. Duis blandit augue ac orci laoreet eget condimentum magna venenatis. Maecenas eget augue in nisl malesuada mollis. Vivamus eget bibendum dolor. Nulla vel varius mi. In hac habitasse platea dictumst. Duis</p>
<div class="abs divider"></div>

<aside class="abs aside">
  <div class="aside-card">
    <div class="aside-mark"><span></span></div>
    <div class="aside-title">Velmory Travel</div>
  </div>
  <p class="aside-text">Duis ac nisi et libero suscipit lobortis ac at velit. Cum sociis natoque penatibus et magnis dis parturient montes, nascetur ridiculus mus. Suspendisse ac nibh id magna adipiscing venenatis ac eu eros. Morbi euismod auctor ipsum, eget mollis eros</p>
  <span class="aside-more">View more →</span>
</aside>

<section class="abs gallery">
  <article class="card" style="left:31px">
    <div class="card-photo" role="img" aria-label="Photo of a smiling family on holiday" style="background:linear-gradient(135deg,#e84a7a,#f4c48a 50%,#d9d2c6)"></div>
    <h4 class="card-title">Lorem Lipsum</h4>
    <p class="card-text">Lorem Ipsum is simply dummy text of the printing and typesetting industry. Lorem</p>
  </article>
  <article class="card" style="left:245px">
    <div class="card-photo" role="img" aria-label="Photo of a tropical island with a longtail boat on turquoise water" style="background:linear-gradient(#3f8fd6,#2e7a3a 45%,#3fc6d8 60%,#a9e4ee)"></div>
    <h4 class="card-title">Lorem Lipsum</h4>
    <p class="card-text">Lorem Ipsum is simply dummy text of the printing and typesetting industry. Lorem</p>
  </article>
  <article class="card" style="left:457px">
    <div class="card-photo" role="img" aria-label="Photo of limestone cliffs and boats on a sandy beach" style="background:linear-gradient(#6fa6d6,#7a7a5a 45%,#5aa0a8 65%,#c8b48a)"></div>
    <h4 class="card-title">Lorem Lipsum</h4>
    <p class="card-text">Lorem Ipsum is simply dummy text of the printing and typesetting industry. Lorem</p>
  </article>
  <article class="card" style="left:673px">
    <div class="card-photo" role="img" aria-label="Photo of a hiker overlooking a blue bay from a cliff" style="background:linear-gradient(#9fc4e6,#3a7ab8 50%,#2a5a8a 70%,#4a4a3a)"></div>
    <h4 class="card-title">Lorem Lipsum</h4>
    <p class="card-text">Lorem Ipsum is simply dummy text of the printing and typesetting industry. Lorem</p>
  </article>
</section>
<div class="abs arrow" style="left:94px;top:1009px"><svg width="10" height="14"><path d="M8 1 2 7l6 6" fill="none" stroke="#fff" stroke-width="2.5"/></svg></div>
<div class="abs arrow" style="left:982px;top:1004px"><svg width="10" height="14"><path d="M2 1l6 6-6 6" fill="none" stroke="#fff" stroke-width="2.5"/></svg></div>

<footer class="abs footer">Copyright © 2013 . All rights reserved •</footer>
</body>
</html>
```